Talent Management Company Needs Business Cards

Using one of the logos provided (attached) K&R Talent Collective needs a business card designed.
Please visit our website for more information about us-

www.krtalentcollective.example

The face should feature a dramatic presentation of the logo with the back being reserved for our professional information which is:

The information should be:
Dorian T. Vickers
C.E.O
Email: dtvickers@krtalentcollective.example
Mobile: 555-804-2917
Website: www.krtalentcollective.example

Marcus L. Vickers
Director of Public Relations
Email: mlvickers@krtalentcollective.example
Mobile: 555-806-3350

Jules R. Hampton
Director of Client Development
Email: jhampton@krtalentcollective.example

Simon Hurlock
Director of Brand Development
Email: shurlock@krtalentcollective.example

Would like the logo to have color. I would like to see one side red or black and the other side white but if it looks better in either black or red that would be fine to but would like to see how it comes out.

Please feel free to message me and if you would like just the icon alone I have other image files that I can send as well.

Target Market(s)

Professional Athletes, coaches, entertainers age 18-35 but also must be accepted in the business community

Industry/Entity Type

Business

Requirements
Must have
• 1) Use the logo
2) Double sided
3) Distinctive
Nice to have
• Small simple images for telephone, e-mail, and Url.

```html
<!DOCTYPE html>
<html lang="en">
<head>
<meta charset="utf-8">
<title>K&amp;R Talent Collective — Business Cards</title>
<link href="https://fonts.googleapis.com/css2?family=Source+Sans+3:wght@400;600&display=swap" rel="stylesheet">
<style>
  :root {
    --backdrop: #3b3b3b;
    --card-light: #f4f4f4;
    --card-dark: #232323;
    --ink: #2a2a2a;
    --ink-soft: #3c3c3c;
    --brand-red: #c4161c;
    --band-dark: #1e1e1e;
    --band-light: #f2f2f2;
  }
  * { margin: 0; padding: 0; box-sizing: border-box; }
  html, body {
    width: 1200px; height: 900px; overflow: hidden;
    background: var(--backdrop);
    font-family: "Source Sans 3", "Myriad Pro", Arial, sans-serif;
  }
  .canvas { position: relative; width: 1200px; height: 900px; }
  .card {
    position: absolute; width: 525px; height: 299px;
    border-radius: 20px; overflow: hidden;
    box-shadow: 0 4px 14px rgba(0,0,0,.35);
  }
  .card--light { background: var(--card-light); color: var(--ink); }
  .card--dark { background: var(--card-dark); color: #fff; }
  .pos-tl { left: 58px;  top: 132px; }
  .pos-tr { left: 617px; top: 132px; }
  .pos-bl { left: 58px;  top: 471px; }
  .pos-br { left: 617px; top: 471px; }

  .brand {
    position: absolute; left: 47px; top: 40px;
    display: flex; flex-direction: column; align-items: center; gap: 10px;
  }
  .brand__dot { width: 44px; height: 44px; border-radius: 50%; background: var(--brand-red); }
  .brand__name {
    font-size: 17px; font-weight: 400; letter-spacing: .2px;
    color: var(--ink); text-transform: uppercase; white-space: nowrap;
  }

  .contact { position: absolute; left: 47px; top: 162px; }
  .contact__name { font-size: 21px; font-weight: 400; color: var(--brand-red); line-height: 1; }
  .contact__title { font-size: 12px; color: var(--ink-soft); margin-top: 6px; }
  .contact__list { list-style: none; margin-top: 16px; }
  .contact__item {
    display: flex; align-items: center; gap: 6px;
    font-size: 12px; color: var(--ink); height: 19px;
  }
  .contact__icon { width: 13px; height: 13px; flex: none; }

  .accent-band {
    position: absolute; right: -40px; top: -20px;
    width: 110px; height: 360px; background: var(--band-dark);
    transform: rotate(14deg);
  }
  .accent-band--light {
    left: -60px; right: auto; width: 120px; background: var(--band-light);
    transform: rotate(-14deg);
  }

  .face-brand {
    position: absolute; left: 0; right: 0; top: 72px;
    display: flex; flex-direction: column; align-items: center; gap: 22px;
  }
  .face-brand .brand__dot { width: 86px; height: 86px; }
  .face-brand__name {
    font-size: 25px; font-weight: 400; color: #fff;
    text-transform: uppercase; letter-spacing: .3px; white-space: nowrap;
    padding-left: 60px;
  }
</style>
</head>
<body>
<main class="canvas">

  <section class="card card--light pos-tl" aria-label="Back of card, Dorian T. Vickers">
    <div class="accent-band"></div>
    <div class="brand"><span class="brand__dot"></span><span class="brand__name">K&amp;R Talent Collective</span></div>
    <div class="contact">
      <p class="contact__name">Dorian T. Vickers</p>
      <p class="contact__title">C.E.O</p>
      <ul class="contact__list">
        <li class="contact__item"><svg class="contact__icon" viewBox="0 0 14 14"><rect x="1" y="3" width="12" height="8" fill="#c4161c"/><path d="M1 3l6 5 6-5" fill="none" stroke="#fff" stroke-width="1.2"/></svg>dtvickers@krtalentcollective.example</li>
        <li class="contact__item"><svg class="contact__icon" viewBox="0 0 14 14"><rect x="4" y="1" width="6" height="12" rx="1.2" fill="#c4161c"/><rect x="5.2" y="2.6" width="3.6" height="6.6" fill="#fff"/></svg>555 804 2917</li>
        <li class="contact__item"><svg class="contact__icon" viewBox="0 0 14 14"><rect width="14" height="14" rx="2" fill="#c4161c"/><circle cx="7" cy="7" r="4" fill="none" stroke="#fff" stroke-width="1.2"/><path d="M3 7h8M7 3v8" stroke="#fff" stroke-width="1"/></svg>www.krtalentcollective.example</li>
      </ul>
    </div>
  </section>

  <section class="card card--light pos-tr" aria-label="Back of card, Dorian T. Vickers">
    <div class="accent-band"></div>
    <div class="brand"><span class="brand__dot"></span><span class="brand__name">K&amp;R Talent Collective</span></div>
    <div class="contact">
      <p class="contact__name">Dorian T. Vickers</p>
      <p class="contact__title">C.E.O</p>
      <ul class="contact__list">
        <li class="contact__item"><svg class="contact__icon" viewBox="0 0 14 14"><rect x="1" y="3" width="12" height="8" fill="#c4161c"/><path d="M1 3l6 5 6-5" fill="none" stroke="#fff" stroke-width="1.2"/></svg>dtvickers@krtalentcollective.example</li>
        <li class="contact__item"><svg class="contact__icon" viewBox="0 0 14 14"><rect x="4" y="1" width="6" height="12" rx="1.2" fill="#c4161c"/><rect x="5.2" y="2.6" width="3.6" height="6.6" fill="#fff"/></svg>555 804 2917</li>
        <li class="contact__item"><svg class="contact__icon" viewBox="0 0 14 14"><rect width="14" height="14" rx="2" fill="#c4161c"/><circle cx="7" cy="7" r="4" fill="none" stroke="#fff" stroke-width="1.2"/><path d="M3 7h8M7 3v8" stroke="#fff" stroke-width="1"/></svg>www.krtalentcollective.example</li>
      </ul>
    </div>
  </section>

  <section class="card card--light pos-bl" aria-label="Back of card, Simon Hurlock">
    <div class="accent-band"></div>
    <div class="brand"><span class="brand__dot"></span><span class="brand__name">K&amp;R Talent Collective</span></div>
    <div class="contact">
      <p class="contact__name">Simon Hurlock</p>
      <p class="contact__title">Director of Brand Development</p>
      <ul class="contact__list">
        <li class="contact__item"><svg class="contact__icon" viewBox="0 0 14 14"><rect x="1" y="3" width="12" height="8" fill="#c4161c"/><path d="M1 3l6 5 6-5" fill="none" stroke="#fff" stroke-width="1.2"/></svg>shurlock@krtalentcollective.example</li>
        <li class="contact__item"><svg class="contact__icon" viewBox="0 0 14 14"><rect x="4" y="1" width="6" height="12" rx="1.2" fill="#c4161c"/><rect x="5.2" y="2.6" width="3.6" height="6.6" fill="#fff"/></svg>555 000 0000</li>
        <li class="contact__item"><svg class="contact__icon" viewBox="0 0 14 14"><rect width="14" height="14" rx="2" fill="#c4161c"/><circle cx="7" cy="7" r="4" fill="none" stroke="#fff" stroke-width="1.2"/><path d="M3 7h8M7 3v8" stroke="#fff" stroke-width="1"/></svg>www.krtalentcollective.example</li>
      </ul>
    </div>
  </section>

  <section class="card card--dark pos-br" aria-label="Front of card">
    <div class="accent-band accent-band--light"></div>
    <div class="face-brand">
      <span class="brand__dot"></span>
      <span class="face-brand__name">K&amp;R Talent Collective</span>
    </div>
  </section>

</main>
</body>
</html>
```